Bright Harbour Fitness

BRIGHT HARBOUR FITNESS PTY LTD, We are a revolutionary, fresh, new entity to the fitness industry looking to make a mark within and support local communities where we are situated. My business partner and i come with a broad range of skill sets and possess the ability and motivation to ensure our philosophy works - and the philosophy is simple - to help people improve their everyday life and well-being. Be it, helping them with their health and fitness, changing their appearance, improving motivation, setting and achieving goals or by helping them become part of a positive team atmosphere.
Our stores visual appearance, like our training concepts, is quite different to the normal run of the mill gym. It's fresh, it's vibrant, it looks great, and we know it will be a real head turner guaranteed to attract attention. This is definitely the future of fitness.
We would like to see on one side our Info and on the other side our LOGO, colour scheme is in the LOGO.
Final design should tell people "We Help People Look And Feel Bright As The Harbour!

Industry/Entity Type

Training

Contact Information for Business Card

Corwin
0412 386 054
cor@brightharbourfitness.com.au
217 Kestrelvale Rd North Manly NSW 2100

Requirements
Must have
• Our Logo

```html
<!DOCTYPE html>
<html lang="en">
<head>
<meta charset="utf-8">
<title>Bright Harbour Fitness – Business Card</title>
<link href="https://fonts.googleapis.com/css2?family=Montserrat:wght@700;800&family=Questrial&display=swap" rel="stylesheet">
<style>
  :root {
    --page: #e9e6e2;
    --card: #050505;
    --gold: #d9b43a;
    --gold-soft: #c9a534;
    --grey: #8a8a8a;
    --grey-dark: #6f6f6f;
    --divider: #3a3a3a;
    --accent-blue: #1f8fd1;
  }
  html, body {
    margin: 0;
    padding: 0;
    width: 1200px;
    height: 900px;
    overflow: hidden;
    background: var(--page);
  }
  .canvas {
    position: relative;
    width: 1200px;
    height: 900px;
  }
  .card {
    position: absolute;
    width: 620px;
    height: 354px;
    background: var(--card);
    border-radius: 22px;
    box-shadow: 0 10px 30px rgba(0,0,0,0.25);
    overflow: hidden;
  }

  /* Front */
  .card--front { left: 110px; top: 60px; }
  .tagline {
    position: absolute;
    right: 42px;
    top: 70px;
    margin: 0;
    font-family: "Montserrat", sans-serif;
    font-weight: 700;
    font-size: 24px;
    color: var(--gold);
  }
  .website {
    position: absolute;
    right: 64px;
    top: 118px;
    margin: 0;
    font-family: "Montserrat", sans-serif;
    font-weight: 700;
    font-size: 15px;
    color: var(--gold-soft);
  }
  .brand-large {
    position: absolute;
    left: 40px;
    bottom: 40px;
    display: flex;
    align-items: center;
    gap: 16px;
  }
  .brand-large .brand-square {
    width: 96px;
    height: 96px;
    background: var(--gold);
    border-radius: 6px;
  }
  .brand-large .brand-name {
    font-family: "Montserrat", sans-serif;
    font-weight: 800;
    font-size: 26px;
    line-height: 1.05;
    color: var(--gold);
    text-transform: uppercase;
  }

  /* Back */
  .card--back { left: 470px; top: 486px; }
  .brand-small {
    position: absolute;
    left: 40px;
    top: 0;
    bottom: 0;
    width: 230px;
    display: flex;
    flex-direction: column;
    align-items: center;
    justify-content: center;
    gap: 16px;
  }
  .brand-small .brand-square {
    width: 70px;
    height: 70px;
    background: var(--gold);
    border-radius: 5px;
  }
  .brand-small .brand-name {
    font-family: "Montserrat", sans-serif;
    font-weight: 800;
    font-size: 24px;
    line-height: 1.05;
    text-align: center;
    color: var(--gold);
    text-transform: uppercase;
  }
  .divider {
    position: absolute;
    left: 300px;
    top: 50px;
    bottom: 50px;
    width: 1px;
    background: var(--divider);
  }
  .person-name {
    position: absolute;
    right: 48px;
    top: 48px;
    margin: 0;
    font-family: "Montserrat", sans-serif;
    font-weight: 700;
    font-size: 17px;
    color: var(--grey-dark);
  }
  .contact-list {
    position: absolute;
    left: 330px;
    top: 170px;
    margin: 0;
    padding: 0;
    list-style: none;
    font-family: "Questrial", sans-serif;
    font-size: 13px;
    color: var(--grey);
  }
  .contact-list li {
    display: flex;
    align-items: center;
    gap: 10px;
    margin-bottom: 16px;
  }
  .contact-icon { width: 11px; height: 11px; flex: none; }
</style>
</head>
<body>
<main class="canvas">

  <section class="card card--front">
    <p class="tagline">Look And Feel Bright As The Harbour!!!</p>
    <p class="website">www.brightharbourfitness.com.au</p>
    <div class="brand-large">
      <div class="brand-square"></div>
      <div class="brand-name">Bright<br>Harbour<br>Fitness</div>
    </div>
  </section>

  <section class="card card--back">
    <div class="brand-small">
      <div class="brand-square"></div>
      <div class="brand-name">Bright Harbour<br>Fitness</div>
    </div>
    <div class="divider"></div>
    <p class="person-name">Corwin</p>
    <ul class="contact-list">
      <li>
        <svg class="contact-icon" viewBox="0 0 12 12" aria-hidden="true">
          <path d="M3 1 L5 3.5 L4 5 Q5 7 7 8 L8.5 7 L11 9 L9.5 11 Q4 10.5 1 3 Z" fill="var(--accent-blue)"/>
        </svg>
        <span>0412 386 054</span>
      </li>
      <li>
        <svg class="contact-icon" viewBox="0 0 12 12" aria-hidden="true">
          <circle cx="6" cy="6" r="2" fill="none" stroke="var(--accent-blue)" stroke-width="1.3"/>
          <path d="M8 4 V7 Q8 8.5 9.5 8 Q11 7 10.7 5 A4.8 4.8 0 1 0 8 10.3" fill="none" stroke="var(--accent-blue)" stroke-width="1.3"/>
        </svg>
        <span>cor@brightharbourfitness.com.au</span>
      </li>
      <li>
        <svg class="contact-icon" viewBox="0 0 12 12" aria-hidden="true">
          <path d="M6 11.5 Q2 7 2 4.5 A4 4 0 0 1 10 4.5 Q10 7 6 11.5 Z" fill="var(--accent-blue)"/>
          <circle cx="6" cy="4.5" r="1.5" fill="var(--card)"/>
        </svg>
        <span>217 Kestrelvale Rd North Manly NSW 2100</span>
      </li>
    </ul>
  </section>

</main>
</body>
</html>
```